Brantor Energy Services Website - Solar Sales and Installation and Renewable Energy Marketing

I need a website for my solar sales and installation/renewable energy marketing company. We will focus on solar, so the web page should make that a main focus. Ideally it will have 5-6 total pages. One main page, one page "Why Solar", "Our Services", "About Us", "Contact Us", and some type of page that collects leads or information from customers who are interested in a solar quote. Our image focus should be either residential solar panels or windmills (renewable energy). The logo, attached, is green and orange. The color scheme should be predominantly white, clean cut, with orange/green buttons or accents. I don't want to have a blog-like page, it should mimic other solar company websites. A good example would be Calderby's solar website.

```html
<!DOCTYPE html>
<html lang="en">
<head>
<meta charset="utf-8">
<title>Brantor Energy Services</title>
<link href="https://fonts.googleapis.com/css2?family=Roboto:wght@300;400;500;700&display=swap" rel="stylesheet">
<style>
:root{
  --orange:#ff7200;
  --green:#7ed321;
  --ink:#1d1d1d;
  --text:#8a8a8a;
  --light:#f5f6f8;
  --line:#e6e6e6;
  --dark:#2b2b2b;
}
*{margin:0;padding:0;box-sizing:border-box}
html,body{width:1200px;height:3548px;overflow:hidden}
body{font-family:'Roboto',sans-serif;color:var(--ink);background:#fff;position:relative}
.abs{position:absolute}
.section{position:absolute;left:0;width:1200px}
.btn{position:absolute;background:var(--orange);color:#fff;font-size:12px;font-weight:500;text-transform:uppercase;display:flex;align-items:center;justify-content:center;letter-spacing:.3px}
.label{position:absolute;color:var(--orange);font-size:12px;font-weight:500;text-transform:uppercase}

/* header */
.topbar{top:0;height:96px;border-bottom:1px solid var(--line)}
.brand{position:absolute;left:127px;top:30px;display:flex;align-items:center;gap:10px}
.brand-dot{width:36px;height:36px;border-radius:50%;background:var(--orange)}
.brand-name{font-size:15px;font-weight:500;color:var(--ink)}
.info{position:absolute;top:30px;display:flex;gap:12px}
.info svg{margin-top:6px}
.info b{display:block;font-size:14px;font-weight:500}
.info span{display:block;font-size:11px;color:var(--text);margin-top:5px}
.nav{top:96px;height:51px;border-bottom:1px solid var(--line)}
.nav-item{position:absolute;top:0;height:51px;border-left:1px solid var(--line);display:flex;align-items:center;justify-content:center;font-size:11.5px;font-weight:500;text-transform:uppercase;color:var(--ink)}
.nav-item.active{color:var(--orange)}

/* hero */
.hero{top:147px;height:601px;background:linear-gradient(115deg,#c7d8e0 0%,#a9cbdf 35%,#6fa9d3 65%,#3b6fa8 85%,#254d86 100%)}
.hero-label{position:absolute;left:124px;top:119px;font-size:14px;font-weight:500;letter-spacing:1.3px;display:flex;align-items:center;gap:12px}
.hero-label i{display:block;width:84px;height:2px;background:var(--orange)}
.hero-label em{font-style:normal;color:var(--orange);font-size:13px}
.hero h1{position:absolute;left:124px;top:162px;font-size:48px;font-weight:700;line-height:51px;color:#1d2b33}
.dots{position:absolute;left:570px;top:467px;display:flex;gap:19px}
.dots i{width:10px;height:10px;border-radius:50%;border:2px solid #fff}
.dots i.on{background:var(--orange);border-color:var(--orange)}
.features{top:670px;left:124px;width:951px;height:78px;background:#fff;border-top:3px solid var(--green);position:absolute}
.feat{position:absolute;top:17px;display:flex;gap:17px}
.feat .ic{width:52px;height:52px;border-radius:50%;background:var(--ink);display:flex;align-items:center;justify-content:center}
.feat .ic.or{background:var(--orange)}
.feat b{display:block;font-size:15px;font-weight:500;margin-top:6px}
.feat b.or{color:var(--orange)}
.feat span{display:block;font-size:13.5px;color:var(--text);margin-top:5px}

/* about */
.about-title{position:absolute;left:122px;top:906px;font-size:35px;font-weight:500;line-height:41px}
.about-text{position:absolute;left:124px;top:1004px;width:460px;font-size:15.5px;line-height:31px;color:var(--text)}
.checks{position:absolute;left:124px;top:1148px;list-style:none;font-size:15.5px;line-height:31px;color:var(--text)}
.checks li::before{content:"›";color:var(--orange);margin-right:14px;font-weight:700}
.about-photo{position:absolute;left:693px;top:907px;width:382px;height:427px;background:linear-gradient(135deg,#9a6e55 0%,#d9cfc6 45%,#8d97a3 70%,#e4e4e2 100%)}
.badge{position:absolute;left:623px;top:1127px;width:128px;height:171px;background:var(--orange);color:#fff;padding:20px 24px}
.badge b{display:block;font-size:20px;font-weight:500;margin-top:14px}
.badge span{display:block;font-size:11.5px;line-height:18px;margin-top:4px}

/* why */
.why{top:1419px;height:613px;background:var(--light)}
.center{text-align:center;left:0;width:1200px}
.sec-title{position:absolute;font-size:36px;font-weight:500;line-height:41px;text-align:center;left:0;width:1200px}
.card{position:absolute;top:228px;width:219px;height:299px;background:#fff;text-align:center}
.card .ic{width:69px;height:69px;border-radius:50%;background:var(--orange);margin:46px auto 0;display:flex;align-items:center;justify-content:center}
.card .ic.dk{background:var(--ink)}
.card h3{font-size:18.5px;font-weight:500;margin-top:23px}
.card p{font-size:13.5px;line-height:22px;color:var(--text);margin:14px 22px 0}

/* services */
.services{top:2032px;height:683px;background:#fff}
.svc{position:absolute;top:186px;width:300px;height:428px;background:var(--light);text-align:center}
.svc .ph{height:214px}
.svc small{display:block;font-size:10px;text-transform:uppercase;margin-top:44px;letter-spacing:.3px}
.svc h3{font-size:18.5px;font-weight:500;margin-top:6px}
.svc p{font-size:13.5px;line-height:25px;color:var(--text);margin:10px 26px 0}
.svc a{display:block;font-size:10.5px;font-weight:700;text-transform:uppercase;margin-top:16px;color:var(--ink);text-decoration:none}
.svc.hot{background:var(--orange);color:#fff}
.svc.hot p,.svc.hot a{color:#fff}

/* cta */
.cta{top:2735px;height:173px;background:var(--orange)}
.cta h2{position:absolute;left:124px;top:45px;color:#fff;font-size:29px;font-weight:500;line-height:41px}
.cta-btn{position:absolute;left:817px;top:61px;width:256px;height:50px;background:#fff;color:var(--orange);font-size:13.5px;letter-spacing:1px;display:flex;align-items:center;justify-content:center;text-transform:uppercase}

/* contact */
.contact{top:2908px;height:555px}
.contact-scene{position:absolute;left:0;top:0;width:600px;height:555px;background:linear-gradient(180deg,#3a3a3a 0%,#555 45%,#2c2c2c 75%,#1b1b1b 100%)}
.contact-info{position:absolute;left:171px;top:0;color:#fff}
.contact-info h4{position:absolute;top:84px;font-size:21px;font-weight:400;white-space:nowrap}
.contact-info .call{position:absolute;top:128px;font-size:32px;font-weight:300;white-space:nowrap}
.contact-info .call b{color:var(--orange);font-weight:400}
.contact-info .mail{position:absolute;top:170px;font-size:15px;color:#ddd}
.contact-info dl{position:absolute;top:218px;font-size:14px;width:300px}
.contact-info dt{font-size:15px;margin-top:0}
.contact-info dd{font-size:13px;line-height:21px;color:#ccc}
.quote{position:absolute;left:600px;top:0;width:600px;height:555px;background:#f1f1f1}
.quote h4{position:absolute;left:85px;top:84px;font-size:20px;font-weight:500}
.field{position:absolute;left:85px;width:343px;height:35px;background:#fff;font-size:12px;color:#aaa;padding:10px 16px}

/* footer */
.footer{top:3463px;height:85px}
.copy{position:absolute;left:171px;top:36px;font-size:13.5px;color:var(--ink)}
.copy span{color:var(--orange)}
.social{position:absolute;left:901px;top:26px;display:flex;gap:10px}
.social i{width:34px;height:34px;border-radius:50%;background:#c4c4c4;display:block}
</style>
</head>
<body>

<header class="section topbar">
  <div class="brand"><span class="brand-dot"></span><span class="brand-name">Brantor Energy Services</span></div>
  <div class="info" style="left:513px">
    <svg width="20" height="20" viewBox="0 0 24 24"><path d="M12 2a7 7 0 0 0-7 7c0 5 7 13 7 13s7-8 7-13a7 7 0 0 0-7-7zm0 9.5A2.5 2.5 0 1 1 12 6.5a2.5 2.5 0 0 1 0 5z" fill="var(--orange)"/></svg>
    <div><b>Harlow Bay</b><span>Kestrel Row, 1230 Avenfield</span></div>
  </div>
  <div class="info" style="left:714px">
    <svg width="20" height="20" viewBox="0 0 24 24"><path d="M3 6h18v12H3z" fill="var(--orange)"/><path d="M3 6l9 7 9-7" fill="none" stroke="#fff" stroke-width="1.6"/></svg>
    <div><b>mail@example.com</b><span>Office Hour: 09:00am - 4:00pm</span></div>
  </div>
  <div class="info" style="left:950px">
    <svg width="20" height="20" viewBox="0 0 24 24"><path d="M6.6 10.8a15 15 0 0 0 6.6 6.6l2.2-2.2c.3-.3.7-.4 1-.2 1.1.4 2.3.6 3.6.6.6 0 1 .4 1 1V20c0 .6-.4 1-1 1A17 17 0 0 1 3 4c0-.6.4-1 1-1h3.5c.6 0 1 .4 1 1 0 1.3.2 2.5.6 3.6.1.3 0 .7-.2 1z" fill="var(--orange)"/></svg>
    <div><b>000 8888 999</b><span>Free Call</span></div>
  </div>
</header>

<nav class="section nav">
  <div class="nav-item active" style="left:125px;width:112px">Home</div>
  <div class="nav-item" style="left:237px;width:110px">About Us</div>
  <div class="nav-item" style="left:347px;width:115px">Our Services</div>
  <div class="nav-item" style="left:462px;width:106px">Why Solar</div>
  <div class="nav-item" style="left:568px;width:115px;border-right:1px solid var(--line)">Contact Us</div>
  <div class="nav-item" style="left:889px;width:49px">
    <svg width="16" height="16" viewBox="0 0 24 24"><circle cx="10" cy="10" r="6.5" fill="none" stroke="var(--orange)" stroke-width="2.4"/><path d="M15 15l6 6" stroke="var(--orange)" stroke-width="2.6"/></svg>
  </div>
  <div class="nav-item" style="left:938px;width:137px;background:var(--orange);color:#fff;text-transform:none;font-weight:400;font-size:12.5px;border:0">Get Free Quote</div>
</nav>

<section class="section hero" role="img" aria-label="Wind turbines beside a tiled roof covered with solar panels under a blue sky">
  <div class="hero-label">CONSERVATION MEANS <i></i><em>01</em></div>
  <h1>Light Up With Solar &amp;<br>Save Natural Resources</h1>
  <div class="btn" style="left:124px;top:301px;width:138px;height:51px">Read More</div>
  <div class="dots"><i></i><i class="on"></i><i></i></div>
</section>

<div class="features">
  <div class="feat" style="left:34px">
    <div class="ic"><svg width="22" height="22" viewBox="0 0 24 24"><circle cx="9" cy="8" r="3" fill="none" stroke="#fff" stroke-width="1.6"/><circle cx="16" cy="9" r="2.5" fill="none" stroke="#fff" stroke-width="1.6"/><path d="M3 19c0-4 3-6 6-6s6 2 6 6M14 14c3 0 6 1.5 6 5" fill="none" stroke="#fff" stroke-width="1.6"/></svg></div>
    <div><b>Trusted Services</b><span>We are trusted by our clients.</span></div>
  </div>
  <div class="feat" style="left:362px">
    <div class="ic or"><svg width="22" height="22" viewBox="0 0 24 24"><path d="M4 14v-2a8 8 0 0 1 16 0v2" fill="none" stroke="#fff" stroke-width="1.8"/><rect x="3" y="13" width="4" height="6" rx="1" fill="#fff"/><rect x="17" y="13" width="4" height="6" rx="1" fill="#fff"/></svg></div>
    <div><b class="or">24/7 Support</b><span>123 4567 890 - 000 8888 999</span></div>
  </div>
  <div class="feat" style="left:689px">
    <div class="ic"><svg width="22" height="22" viewBox="0 0 24 24"><circle cx="12" cy="6" r="3" fill="none" stroke="#fff" stroke-width="1.6"/><path d="M6 21v-6a6 6 0 0 1 12 0v6z" fill="none" stroke="#fff" stroke-width="1.6"/></svg></div>
    <div><b>Well Experienced</b><span>25 years of experience</span></div>
  </div>
</div>

<div class="label" style="left:125px;top:880px">About Company</div>
<h2 class="about-title">Powering Your Business<br>for Over 25 Years</h2>
<p class="about-text">Lorem ipsum dolor sit amet, consectetur adipiscing elit, sed do eiusmod tempor incididunt ut labore et dolore magna aliqua. Ut enim ad minim veniam, quis nostrud exercitation ullamco laboris nisi ut aliquip ex ea commodo consequat.</p>
<ul class="checks">
  <li>Excepteur sint occaecat cupidatat</li>
  <li>Duis aute irure dolor in reprehenderit</li>
  <li>Deserunt mollit anim id est laborum.</li>
</ul>
<div class="btn" style="left:124px;top:1283px;width:138px;height:51px">Get In Teach</div>
<div class="about-photo" role="img" aria-label="Engineer at a desk examining small model wind turbines"></div>
<div class="badge">
  <svg width="62" height="58" viewBox="0 0 62 58"><circle cx="12" cy="12" r="5" fill="#fff"/><g stroke="#fff" stroke-width="2"><path d="M12 2v3M12 19v3M2 12h3M19 12h3"/><path d="M44 56V18M44 18l-4-14M44 18l12 6M44 18l-10 8"/></g><path d="M6 44h28l-3 10H3z" fill="#fff"/><path d="M12 44v10M20 44v10M6 49h26" stroke="var(--orange)" stroke-width="1.5"/></svg>
  <b>25 Years</b>
  <span>Experience<br>Working</span>
</div>

<section class="section why">
  <div class="label center" style="top:88px">Why Choose Us</div>
  <h2 class="sec-title" style="top:113px">Produce Your Own Clean Save our<br>the Environment</h2>
  <div class="card" style="left:124px">
    <div class="ic"><svg width="30" height="30" viewBox="0 0 24 24"><path d="M12 22V11M12 11L9 3M12 11l8 2M12 11l-7 5" stroke="#fff" stroke-width="1.8" fill="none"/></svg></div>
    <h3>1. Peak Shaving</h3>
    <p>Excepteur sint occaecat cupidatat non proident, sunt in culpa officia deserunt mollit at laborum.</p>
  </div>
  <div class="card" style="left:368px">
    <div class="ic dk"><svg width="30" height="30" viewBox="0 0 24 24"><path d="M4 9l8-4 8 4-8 4zM4 13l8 4 8-4M4 17l8 4 8-4" stroke="#fff" stroke-width="1.6" fill="none"/></svg></div>
    <h3>2. Save Money</h3>
    <p>Excepteur sint occaecat cupidatat non proident, sunt in culpa officia deserunt mollit at laborum.</p>
  </div>
  <div class="card" style="left:612px">
    <div class="ic"><svg width="30" height="30" viewBox="0 0 24 24"><circle cx="12" cy="9" r="6" stroke="#fff" stroke-width="1.6" fill="none"/><path d="M9 9l2 2 4-4M8 14l-2 7 6-3 6 3-2-7" stroke="#fff" stroke-width="1.6" fill="none"/></svg></div>
    <h3>3. 25-year warranty<sup style="font-size:10px">*</sup></h3>
    <p>Excepteur sint occaecat cupidatat non proident, sunt in culpa officia deserunt mollit at laborum.</p>
  </div>
  <div class="card" style="left:857px">
    <div class="ic"><svg width="30" height="30" viewBox="0 0 24 24"><circle cx="12" cy="12" r="9" stroke="#fff" stroke-width="1.6" fill="none"/><path d="M7 13a5 5 0 0 1 9-4M12 12l4-3" stroke="#fff" stroke-width="1.6" fill="none"/></svg></div>
    <h3>4. Installation Included</h3>
    <p>Excepteur sint occaecat cupidatat non proident, sunt in culpa officia deserunt mollit at laborum.</p>
  </div>
</section>

<section class="section services">
  <div class="label center" style="top:82px">Our Services</div>
  <h2 class="sec-title" style="top:108px">We Offer Different Services</h2>
  <div class="svc" style="left:124px">
    <div class="ph" role="img" aria-label="Technicians installing rooftop solar panels" style="background:linear-gradient(180deg,#6f9fd6 0%,#b6cde4 40%,#2f4f9a 60%,#1d3575 100%)"></div>
    <small>Energy</small><h3>Technical Services</h3>
    <p>Lorem ipsum dolor sit amet consem et ctetuering adipisc elit sed diam.</p><a>Read More</a>
  </div>
  <div class="svc hot" style="left:451px">
    <div class="ph" role="img" aria-label="Worker servicing a large solar array" style="background:linear-gradient(180deg,#4d7fc8 0%,#a8c3df 30%,#54688a 50%,#22406f 100%)"></div>
    <small>Electricity</small><h3>Solar As A Service</h3>
    <p>Lorem ipsum dolor sit amet consem et ctetuering adipisc elit sed diam.</p><a>Read More</a>
  </div>
  <div class="svc" style="left:774px">
    <div class="ph" role="img" aria-label="Solar panel field in the sun" style="background:linear-gradient(160deg,#dfe9f3 0%,#8fb0d8 30%,#2f4f99 60%,#4c6b3a 100%)"></div>
    <small>Energy</small><h3>Energy Manufacture</h3>
    <p>Lorem ipsum dolor sit amet consem et ctetuering adipisc elit sed diam.</p><a>Read More</a>
  </div>
</section>

<section class="section cta">
  <h2>Let’s See if Going Solar Is Right<br>for You</h2>
  <div class="cta-btn">Contact Us Today!</div>
</section>

<section class="section contact">
  <div class="contact-scene" role="img" aria-label="Silhouetted wind turbines above a river at dusk"></div>
  <div class="contact-info">
    <h4>Brantor Energy Services</h4>
    <div class="call">Call. <b>000 8888 999</b></div>
    <div class="mail">e.mail@example.com</div>
    <dl>
      <dt>Address:</dt>
      <dd>908, Lorem Road, Northwest<br>Fenway Loop, DM 40217</dd>
      <dt style="margin-top:18px">Office Hours:</dt>
      <dd>Monday to Saturday<br>9:00 - 18:00<br>Sunday: Closed</dd>
    </dl>
    <div class="btn" style="left:0;top:434px;width:154px;height:35px">Contact Us</div>
  </div>
  <div class="quote">
    <h4>Get a free quote</h4>
    <div class="field" style="top:133px">Your Name</div>
    <div class="field" style="top:187px">Email</div>
    <div class="field" style="top:240px">Phone</div>
    <div class="field" style="top:293px;height:86px">Message ...</div>
    <div class="btn" style="left:85px;top:434px;width:154px;height:35px">Submit</div>
  </div>
</section>

<footer class="section footer">
  <div class="copy">© Copyright 2019 <span>Brantor Energy Services.</span></div>
  <div class="social"><i></i><i></i><i></i><i></i><i></i></div>
  <svg class="abs" style="left:1148px;top:33px" width="20" height="22" viewBox="0 0 20 22"><path d="M10 2L2 20l8-5 8 5z" fill="none" stroke="var(--orange)" stroke-width="2"/></svg>
</footer>

</body>
</html>
```